Thoroughbred Racing Partnership needs web design

Crest of Fortune Partners is a management group who buys horses and races them on both the West and East coasts. The premise of the business is for an investment as little as $500, anyone can be a partner and own a percentage of a horse(s). This is a low cost way of getting involved in the exciting sport of Thoroughbred Racing, without shouldering the heavy financial responsibility. Our target market is mostly males 40+ but we want to include all target markets. We are looking for something very clean and professional, we want to give an image of success. Nothing overly "artsy." I have included the logo in which you can incorporate in the site. Also, the logo colors will be the colors of our "silks." The silks are what the jockey wears and will be an important marketing tool for COF. We would like a very prominent picture of a racehorse somewhere on the homepage, we want to make it clear that is a website for Horseracing partnerships.

On the top of the site, it should say "Crest of Fortune" (on the top)
and below that "Thoroughbred Racing Partnerships." (below that)

The main sections, which should be across the top are:

Home
About Us
Ownership
Stable Roster
News
Contact us

Some of these will have drop down menus.

An example of a competitor website that we like is: www.harlowfieldeq.example
An example of a competitor website that we don't like is: www.gallopvane.example
Updates

Project Deadline Extended
Reason: We have a Board of Directors meeting on the 22nd and we will be making a decision on that day. I'm giving an extension so that all designers are able to submit their designs by the 22nd. Thank you!

Target Market(s)

40+ males

Industry/Entity Type

Business

Requirements
Must have
• our logo must be on the site. We would like at least one bold image of a thoroughbred horse in action. The picture is going to tell the story so it needs to be very eye-catching.

Our slogan should also be included on the website, "Experience the thrill of owning a Racehorse."
Should not have
• cartoons, artsy pictures, pictures of Steeplechase horses or "jumpers." This partnership is for racehorses only, there is not jumping involved with the horses.

```html
<!DOCTYPE html>
<html lang="en">
<head>
<meta charset="utf-8">
<title>Crest of Fortune Partners – Thoroughbred Racing Partnerships</title>
<link rel="stylesheet" href="https://fonts.googleapis.com/css2?family=Open+Sans:wght@400;600;700&family=Oswald:wght@400;500&family=Ubuntu:wght@400;500&family=Yanone+Kaffeesatz:wght@500;700&display=swap">
<style>
  :root {
    --black: #000000;
    --header-dark: #0b0b0b;
    --nav-top: #4a4a4a;
    --nav-bottom: #1a1a1a;
    --nav-divider: #5a5a5a;
    --white: #ffffff;
    --gold: #f5b417;
    --gold-deep: #f08a0c;
    --orange-title: #d9780e;
    --body-grey: #7d7d7d;
    --footer-bg: #e6e6e6;
    --footer-text: #3a3a3a;
    --footer-heading: #111111;
    --copyright-bg: #3c3c3c;
    --copyright-text: #b4b4b4;
    --line-grey: #555555;
    --video-frame: #111111;
    --progress: #1aa6e6;
  }
  * { box-sizing: border-box; margin: 0; padding: 0; }
  html, body { width: 1123px; height: 1200px; overflow: hidden; }
  body {
    position: relative;
    background: var(--black);
    font-family: "Open Sans", Arial, sans-serif;
    color: var(--white);
  }

  /* Header */
  .site-header {
    position: absolute; left: 0; top: 0; width: 1123px; height: 118px;
    background: radial-gradient(ellipse at 50% 0%, #2a2a2a 0%, var(--header-dark) 65%);
  }
  .brand {
    position: absolute; left: 132px; top: 14px;
    display: flex; align-items: center; gap: 10px;
    font-family: "Open Sans", Arial, sans-serif; font-weight: 700;
    color: var(--white);
  }
  .brand-mark { width: 16px; height: 16px; border-radius: 50%; background: var(--white); }
  .brand-name { font-size: 22px; line-height: 1.15; letter-spacing: 0.5px; }
  .brand-name small { display: block; font-size: 22px; font-weight: 700; }

  .social { position: absolute; top: 28px; left: 814px; display: flex; gap: 10px; }
  .social span {
    width: 38px; height: 38px; border-radius: 50%;
    background: linear-gradient(#f2f2f2, #bdbdbd);
  }

  .main-nav {
    position: absolute; left: 132px; top: 98px; width: 860px; height: 41px;
    background: linear-gradient(var(--nav-top), var(--nav-bottom));
    border-radius: 4px; display: flex; z-index: 3;
    box-shadow: 0 2px 4px rgba(0,0,0,.6);
  }
  .main-nav a {
    display: flex; align-items: center; justify-content: center;
    color: var(--white); text-decoration: none;
    font-size: 13px; font-weight: 600; letter-spacing: 1px;
    border-right: 1px solid var(--nav-divider);
  }
  .main-nav a:last-child { border-right: none; }

  /* Hero */
  .hero {
    position: absolute; left: 0; top: 118px; width: 1123px; height: 447px;
  }
  .hero-photo {
    position: absolute; inset: 0;
    background:
      linear-gradient(180deg, #dfe6ee 0%, #b9c4cf 12%, #6f8a78 28%, #4f6b3f 44%, #e8e6e2 58%, #cfc3b0 72%, #e2d8c8 100%);
  }
  .hero-title {
    position: absolute; left: 705px; top: 36px; width: 275px; text-align: center;
  }
  .hero-title .rule { height: 2px; background: #2a2a2a; margin: 0 auto; width: 240px; position: relative; }
  .hero-title .rule::after {
    content: ""; position: absolute; left: 50%; top: -4px; width: 8px; height: 8px;
    margin-left: -4px; background: #2a2a2a; transform: rotate(45deg);
  }
  .hero-title h1 {
    font-family: "Oswald", Arial, sans-serif; font-weight: 500;
    font-size: 27px; color: var(--orange-title); letter-spacing: 0.5px;
    margin-top: 10px; line-height: 1.1;
  }
  .hero-title p {
    font-size: 14px; color: #111; margin: 4px 0 14px;
  }

  .video-player {
    position: absolute; left: 677px; top: 138px; width: 315px; height: 220px;
    background: var(--video-frame); padding: 6px;
  }
  .video-frame {
    width: 303px; height: 172px;
    background: linear-gradient(180deg, #8a9a7a 0%, #9fb08e 30%, #d7d7d5 45%, #a9a49c 70%, #8f8a82 100%);
  }
  .video-tools {
    position: absolute; right: 10px; top: 10px; display: flex; flex-direction: column; gap: 4px;
  }
  .video-tools span {
    width: 30px; height: 24px; background: #1d1d1d; border-radius: 2px;
    font-size: 6px; color: #ddd; text-align: center; padding-top: 15px; letter-spacing: .3px;
  }
  .video-controls {
    position: absolute; left: 6px; bottom: 6px; width: 303px; height: 30px;
    display: flex; align-items: center; gap: 8px;
  }
  .play-btn { width: 36px; height: 26px; background: #222; display: flex; align-items: center; justify-content: center; }
  .progress {
    width: 175px; height: 7px; border: 1px solid #666; background: #333; position: relative;
  }
  .progress::before { content: ""; position: absolute; left: 0; top: 0; bottom: 0; width: 60px; background: var(--progress); }
  .progress::after { content: ""; position: absolute; left: 60px; top: 0; bottom: 0; width: 50px; background: #777; }
  .hd { font-size: 11px; font-weight: 700; font-style: normal; color: var(--progress); }

  .cta-ownership {
    position: absolute; left: 693px; top: 373px; width: 290px; height: 54px;
    border-radius: 27px; background: linear-gradient(var(--gold), var(--gold-deep));
    padding: 7px 0 0 28px; color: #111; text-decoration: none;
    box-shadow: 0 2px 3px rgba(0,0,0,.3);
  }
  .cta-ownership strong { display: block; font-size: 19px; font-weight: 600; line-height: 1.1; }
  .cta-ownership span { font-size: 14px; }
  .cta-ownership svg { position: absolute; right: 24px; top: 13px; }

  .slide-dots { position: absolute; top: 427px; left: 500px; display: flex; gap: 13px; }
  .slide-dots span {
    width: 29px; height: 29px; background: var(--white); border: 2px solid #111;
    transform: rotate(45deg); display: flex; align-items: center; justify-content: center;
  }
  .slide-dots b { transform: rotate(-45deg); color: #111; font-size: 15px; font-weight: 600; }

  /* Intro */
  .section-heading {
    font-family: "Oswald", Arial, sans-serif; font-weight: 400;
    color: var(--gold); font-size: 22px; line-height: 27px; letter-spacing: .5px;
  }
  .why { position: absolute; left: 132px; top: 607px; width: 405px; }
  .why p {
    color: var(--body-grey); font-size: 13.5px; line-height: 21px;
    text-align: justify; margin-top: 15px;
  }
  .why p + p { margin-top: 21px; }

  .news { position: absolute; left: 590px; top: 607px; width: 403px; }
  .news-item { margin-top: 14px; }
  .news-item + .news-item { margin-top: 14px; }
  .news-item h3 {
    font-size: 12.5px; font-weight: 700; color: var(--white); display: flex; align-items: center; gap: 8px;
  }
  .news-item p {
    color: var(--body-grey); font-size: 13.5px; line-height: 21px; text-align: justify;
    padding-left: 17px; margin-top: 2px;
  }

  /* Slogan ribbon */
  .slogan-band { position: absolute; left: 132px; top: 876px; width: 860px; height: 50px; }
  .slogan-band .rule { position: absolute; top: 24px; height: 1px; background: var(--line-grey); width: 860px; }
  .slogan-band .rule.second { top: 28px; left: 40px; width: 780px; }
  .slogan-band svg { position: absolute; left: 117px; top: 0; }
  .slogan-band p {
    position: absolute; left: 117px; width: 626px; top: 0; height: 50px; line-height: 50px; text-align: center;
    font-family: "Yanone Kaffeesatz", Arial, sans-serif; font-weight: 500; font-size: 25px;
    color: #1a1a1a; letter-spacing: 1.5px;
  }

  /* Footer */
  .site-footer {
    position: absolute; left: 0; top: 961px; width: 1123px; height: 202px;
    background: var(--footer-bg); color: var(--footer-text);
  }
  .footer-col { position: absolute; top: 24px; }
  .footer-col h4 {
    font-family: "Ubuntu", Arial, sans-serif; font-weight: 400; font-size: 18.5px;
    color: var(--footer-heading); margin-bottom: 10px;
  }
  .footer-about { left: 132px; width: 282px; }
  .footer-about p { font-size: 12.3px; line-height: 21px; text-align: justify; }
  .footer-links { left: 563px; }
  .footer-links li { list-style: none; font-size: 12.3px; line-height: 21px; }
  .footer-links li::before { content: "›"; color: #999; margin-right: 8px; }
  .footer-contact { left: 766px; width: 240px; }
  .footer-contact .lead { font-size: 12.3px; line-height: 21px; color: #111; }
  .contact-line { display: flex; align-items: center; gap: 10px; font-size: 12.3px; margin-top: 5px; line-height: 21px; }
  .contact-line a { color: #111; text-decoration: underline; }
  .contact-line svg { flex: none; }

  .copyright {
    position: absolute; left: 0; top: 1163px; width: 1123px; height: 37px;
    background: var(--copyright-bg); color: var(--copyright-text);
    font-size: 12px; text-align: center; line-height: 37px; font-family: "Ubuntu", Arial, sans-serif;
  }
</style>
</head>
<body>

<header class="site-header">
  <div class="brand">
    <span class="brand-mark"></span>
    <div class="brand-name">COF<small>PARTNERS.COM</small></div>
  </div>
  <div class="social" aria-label="Social links">
    <span></span><span></span><span></span><span></span>
  </div>
</header>

<nav class="main-nav">
  <a href="#" style="width:118px">HOME</a>
  <a href="#" style="width:141px">ABOUT US</a>
  <a href="#" style="width:150px">OWNERSHIP</a>
  <a href="#" style="width:176px">STABLE ROSTER</a>
  <a href="#" style="width:106px">NEWS</a>
  <a href="#" style="width:169px">CONTACT US</a>
</nav>

<section class="hero">
  <div class="hero-photo" role="img" aria-label="Jockey in racing silks riding a galloping thoroughbred along the rail of a dirt track, green hills behind"></div>

  <div class="hero-title">
    <div class="rule"></div>
    <h1>CREST OF FORTUNE</h1>
    <p>"Thoroughbred Racing Partnerships"</p>
    <div class="rule"></div>
  </div>

  <div class="video-player">
    <div class="video-frame" role="img" aria-label="Video still of two racehorses with jockeys on a dirt track"></div>
    <div class="video-tools">
      <span>LIKE</span><span>LATER</span><span>SHARE</span><span>EMBED</span>
    </div>
    <div class="video-controls">
      <div class="play-btn">
        <svg width="12" height="14" viewBox="0 0 12 14"><path d="M1 1 L11 7 L1 13 Z" fill="#fff"/></svg>
      </div>
      <div class="progress"></div>
      <i class="hd">HD</i>
    </div>
  </div>

  <a class="cta-ownership" href="#">
    <strong>New to Ownership</strong>
    <span>Learn about racing Partnership</span>
    <svg width="28" height="28" viewBox="0 0 28 28"><circle cx="14" cy="14" r="12" fill="#fff" stroke="#333" stroke-width="2"/><path d="M11 8 L17 14 L11 20" fill="none" stroke="#1e5fa8" stroke-width="3"/></svg>
  </a>

  <div class="slide-dots">
    <span><b>1</b></span><span><b>2</b></span><span><b>3</b></span>
  </div>
</section>

<section class="why">
  <h2 class="section-heading">WHY CHOOSE<br>HORSE RACING PARTNERSHIPS?</h2>
  <p>Lorem Ipsum is simply dummy text of the printing and typesetting industry. Lorem Ipsum has been the industry's standard dummy text ever since the 1500s, when an unknown printer took a galley of type and scrambled it to make a type specimen book. It has survived not only five centuries.</p>
  <p>It is a long established fact that a reader will be distracted by the readable content of a page when looking at its layout.</p>
</section>

<section class="news">
  <h2 class="section-heading">OUR<br>LATEST NEWS</h2>
  <article class="news-item">
    <h3><svg width="9" height="9" viewBox="0 0 9 9"><path d="M0 4.5 H8 M4.5 1 L8 4.5 L4.5 8" fill="none" stroke="#fff" stroke-width="1.3"/></svg>TOP WINNER OF 2013</h3>
    <p>Lorem Ipsum has been the industry's standard dummy text ever since the 1500s, when an unknown printer took a galley of type and scrambled it to make a type specimen book.</p>
  </article>
  <article class="news-item">
    <h3><svg width="9" height="9" viewBox="0 0 9 9"><path d="M0 4.5 H8 M4.5 1 L8 4.5 L4.5 8" fill="none" stroke="#fff" stroke-width="1.3"/></svg>FORTUNE MANAGEMENT GROUP</h3>
    <p>Lorem Ipsum is simply dummy text of the printing and typesetting industry. when an unknown printer took a galley of type and scrambled it to make a type specimen book.</p>
  </article>
</section>

<div class="slogan-band">
  <div class="rule"></div>
  <div class="rule second"></div>
  <svg width="626" height="50" viewBox="0 0 626 50">
    <defs>
      <linearGradient id="ribbonFill" x1="0" y1="0" x2="0" y2="1">
        <stop offset="0" stop-color="#f7be1d"/>
        <stop offset="1" stop-color="#f08a0c"/>
      </linearGradient>
    </defs>
    <path d="M0 0 H626 L604 25 L626 50 H0 L22 25 Z" fill="url(#ribbonFill)"/>
    <circle cx="38" cy="25" r="6" fill="#111"/>
    <circle cx="588" cy="25" r="6" fill="#111"/>
  </svg>
  <p>"EXPERIENCE THE THRILL OF OWNING A RACEHORSE."</p>
</div>

<footer class="site-footer">
  <div class="footer-col footer-about">
    <h4>About us</h4>
    <p>Lorem Ipsum is simply dummy text of the printing and typesetting industry. Lorem Ipsum has been the industry's standard dummy text ever since the 1500s, when an unknown printer took a galley of type and scrambled it to make a type specimen book. It has survived not only five centuries.</p>
  </div>
  <div class="footer-col footer-links">
    <h4>Quick Links</h4>
    <ul>
      <li>Home</li><li>About US</li><li>Ownership</li><li>Stable Roster</li><li>News</li><li>Contact US</li>
    </ul>
  </div>
  <div class="footer-col footer-contact">
    <h4>Contact info</h4>
    <p class="lead">Lorem ipsum dolor sit amet, consectetur adipiscing elit.</p>
    <div class="contact-line">
      <svg width="12" height="12" viewBox="0 0 12 12"><circle cx="6" cy="3.5" r="3" fill="#999"/><path d="M0 12 C0 7 12 7 12 12 Z" fill="#999"/></svg>
      <span>Lorem ipsum, State, Country</span>
    </div>
    <div class="contact-line">
      <svg width="12" height="12" viewBox="0 0 12 12"><path d="M2 1 L5 1 L6 4 L4 5.5 C5 7.5 6 8.5 7.5 9 L9 7 L12 8 L12 11 C6 12 0 6 1 1 Z" fill="#999"/></svg>
      <span>Tel.: +123 456 7890</span>
    </div>
    <div class="contact-line">
      <svg width="12" height="10" viewBox="0 0 12 10"><rect x="0" y="0" width="12" height="10" fill="#999"/><path d="M0 0 L6 5 L12 0" fill="none" stroke="#e6e6e6" stroke-width="1.2"/></svg>
      <span>E-mail: <a href="#">info@crestoffortune.example</a></span>
    </div>
  </div>
</footer>

<div class="copyright">COPYRIGHT ©2013 CREST OF FORTUNE . ALL RIGHTS RESERVED.</div>

</body>
</html>
```